Health Care Company with Logo Needs Business Cards designed

We are a luxury behavioral health company looking for business cards design we already have a logo and are looking for someone to design a sophisticated luxurious looking business card. Please note that Card design should be captivating just like the logo and also encompass the logo color

Industry/Entity Type

Healthcare

Contact Information for Business Card

Logo,company name, tagline, my name and title, contact details, and physical address

```html
<!DOCTYPE html>
<html lang="en">
<head>
<meta charset="utf-8">
<title>Marlowe Behavioral Health – Business Card</title>
<link href="https://fonts.googleapis.com/css2?family=Arimo:wght@400;700&display=swap" rel="stylesheet">
<style>
  :root {
    --stage: #222222;
    --purple: #7b3a98;
    --purple-deep: #6c2f88;
    --blue: #25a8e0;
    --green: #8cc63f;
    --orange: #f7941d;
    --ink: #222222;
    --paper: #ffffff;
  }
  * { box-sizing: border-box; margin: 0; padding: 0; }
  html, body { width: 1200px; height: 988px; overflow: hidden; }
  body {
    background: var(--stage);
    font-family: "Arimo", Arial, sans-serif;
    position: relative;
  }
  .card {
    position: absolute;
    left: 330px;
    width: 540px;
    height: 309px;
    border-radius: 18px;
    overflow: hidden;
  }
  .card--back { top: 100px; background: var(--purple); }
  .card--front { top: 560px; background: var(--paper); }

  .brand { position: absolute; display: flex; align-items: center; gap: 10px; }
  .brand__mark { width: 30px; height: 30px; flex: none; }
  .brand__name {
    font-weight: 700;
    font-size: 22px;
    line-height: 1;
    letter-spacing: -0.2px;
  }
  .brand__tagline {
    font-size: 7.5px;
    letter-spacing: 2.2px;
    text-transform: uppercase;
    color: var(--blue);
    margin-top: 4px;
    font-weight: 700;
  }
  .card--back .brand { right: 40px; bottom: 40px; }
  .card--back .brand__mark { background: var(--paper); }
  .card--back .brand__name { color: var(--paper); }

  .card--front .brand { right: 40px; top: 40px; }
  .card--front .brand__mark { background: var(--purple); }
  .card--front .brand__name { color: var(--purple); }

  .divider { position: absolute; height: 1px; background: var(--green); }
  .divider--main { left: 160px; right: 30px; top: 118px; }
  .divider--short { left: 40px; width: 170px; top: 196px; }

  .person { position: absolute; left: 40px; top: 140px; }
  .person__name {
    color: var(--purple);
    font-weight: 700;
    font-size: 26px;
    letter-spacing: 0.3px;
    text-transform: uppercase;
  }
  .person__title { color: var(--ink); font-size: 15px; margin-top: 3px; }

  .contacts { position: absolute; left: 40px; top: 206px; list-style: none; }
  .contacts li {
    display: flex; align-items: center; gap: 7px;
    font-size: 13.5px; color: var(--ink); line-height: 17px;
  }
  .contacts svg { width: 11px; height: 11px; fill: var(--blue); flex: none; }

  .address {
    position: absolute; right: 40px; top: 150px;
    text-align: right; font-size: 13.5px; line-height: 18px; color: var(--ink);
  }

  .stripe { position: absolute; left: 0; bottom: 0; width: 540px; height: 22px; }
</style>
</head>
<body>
  <section class="card card--back" aria-label="Card back">
    <div class="brand">
      <span class="brand__mark"></span>
      <div>
        <div class="brand__name">Marlowe Behavioral Health</div>
        <div class="brand__tagline">Dedicated to hope, healing and recovery</div>
      </div>
    </div>
  </section>

  <section class="card card--front" aria-label="Card front">
    <div class="brand">
      <span class="brand__mark"></span>
      <div>
        <div class="brand__name">Marlowe Behavioral Health</div>
        <div class="brand__tagline">Dedicated to hope, healing and recovery</div>
      </div>
    </div>

    <div class="divider divider--main"></div>

    <div class="person">
      <h1 class="person__name">Daniel Reyes</h1>
      <p class="person__title">Founder &amp; CEO</p>
    </div>

    <div class="divider divider--short"></div>

    <ul class="contacts">
      <li><svg viewBox="0 0 24 24"><path d="M6.6 10.8a15.1 15.1 0 0 0 6.6 6.6l2.2-2.2a1 1 0 0 1 1-.25 11.4 11.4 0 0 0 3.6.57 1 1 0 0 1 1 1V20a1 1 0 0 1-1 1A17 17 0 0 1 3 4a1 1 0 0 1 1-1h3.5a1 1 0 0 1 1 1c0 1.25.2 2.45.57 3.57a1 1 0 0 1-.25 1z"/></svg>555-210-4837</li>
      <li><svg viewBox="0 0 24 24"><path d="M6 2h12v5H6zM3 8h18a1 1 0 0 1 1 1v8h-4v5H6v-5H2V9a1 1 0 0 1 1-1zm5 8v4h8v-4z"/></svg>555-210-4838</li>
      <li><svg viewBox="0 0 24 24"><path d="M2 5h20v14H2zm2 2v.5l8 5 8-5V7l-8 5z"/></svg>hello@marlowebehavioral.com</li>
      <li><svg viewBox="0 0 24 24"><circle cx="12" cy="12" r="10"/></svg>www.marlowebehavioral.com</li>
    </ul>

    <address class="address" style="font-style:normal">
      2780 Linden Park Road Suite 140<br>
      Ashford, TN 37190
    </address>

    <svg class="stripe" viewBox="0 0 540 22" preserveAspectRatio="none" aria-hidden="true">
      <polygon points="0,0 137,0 130,22 0,22" fill="var(--blue)"/>
      <polygon points="141,0 290,0 283,22 134,22" fill="var(--purple)"/>
      <polygon points="294,0 420,0 413,22 287,22" fill="var(--green)"/>
      <polygon points="424,0 540,0 540,22 417,22" fill="var(--orange)"/>
    </svg>
  </section>
</body>
</html>
```